Harbourline Strategy Group firm

I need a business card that is succint for a Brisbane based business called Harbourline Strategy Group Pty Ltd.
We bridge the gaps between People, Process and Technology.

We are a specialist operational excellence firm, delivering strategic consulting and business advisory services in six core capabilities, across all industries and all business lines to improve performance, efficiency, profitability, automation and scalability, for clients across Australia &New Zealand.
Updates

Hi Designers, I have uploaded the logo in 3D .png format, to assist in card design.

Target Market(s)

Project Management professionals, IT professionals, corporate and government clients managing transitioning or transformation projects.

Contact Information for Business Card

Harbourline Strategy Group Pty Ltd

Daniel Ferreira
Principal Consultant

mobile: +61 417 260 315
email: daniel@harbourlinestrategygroup.com.au
webpage: www.harbourlinestrategygroup.com

professional services: strategic advisors,

Font styles to use
Sans Serif

Requirements
Must have
• Business name: Harbourline Strategy Group
logo: attached
Contact person: Daniel Ferreira
Title: Principal Consultant
contact details:
mobile +61 417 260
email: daniel@HarbourlineStrategyGroup.com.au
website: HarbourlineStrategyGroup.com

on back side with logo include: A.B.N. 58210947362

professional services offered: Business Analysis, Strategic Advisory
Nice to have
• QR code
Should not have
• contacts picture

```html
<!DOCTYPE html>
<html lang="en">
<head>
<meta charset="utf-8">
<title>Harbourline Strategy Group – Business Card</title>
<link rel="stylesheet" href="https://fonts.googleapis.com/css2?family=Montserrat:wght@500;700&family=Open+Sans:wght@400;600&display=swap">
<style>
  :root {
    --navy: #2a3352;
    --red: #e3262f;
    --grey: #5b5e67;
    --paper: #ffffff;
    --backdrop: #e9e7e3;
  }
  * { box-sizing: border-box; margin: 0; padding: 0; }
  html, body {
    width: 1200px; height: 1024px; overflow: hidden;
    background: var(--backdrop);
  }
  .canvas {
    width: 1200px; height: 1024px;
    display: flex; flex-direction: column; align-items: center; justify-content: center;
    gap: 28px;
  }
  .card {
    position: relative;
    width: 820px; height: 468px;
    background: var(--paper);
    box-shadow: 0 6px 18px rgba(0,0,0,0.18);
  }

  /* Front */
  .brand {
    position: absolute; left: 64px; top: 58px;
    display: flex; align-items: center; gap: 16px;
  }
  .brand-square { width: 34px; height: 34px; background: var(--red); }
  .brand-name {
    font-family: "Montserrat", sans-serif; font-weight: 700;
    color: var(--navy); font-size: 30px; line-height: 1.02; letter-spacing: 0.5px;
    text-transform: uppercase;
  }
  .person { position: absolute; left: 64px; top: 206px; }
  .person-name {
    font-family: "Montserrat", sans-serif; font-weight: 500;
    font-size: 30px; color: var(--grey); letter-spacing: 1.5px; text-transform: uppercase;
  }
  .person-title {
    font-family: "Open Sans", sans-serif; font-weight: 600;
    font-size: 21px; color: var(--red); margin-top: 2px;
  }
  .contacts {
    position: absolute; left: 64px; top: 306px;
    list-style: none; display: flex; flex-direction: column; gap: 10px;
  }
  .contact {
    display: flex; align-items: center; gap: 14px;
    font-family: "Open Sans", sans-serif; font-size: 22px; color: var(--navy);
  }
  .contact svg { width: 22px; height: 22px; flex: none; }

  /* Back */
  .back-brand {
    position: absolute; right: 60px; bottom: 92px;
    text-align: right;
    font-family: "Montserrat", sans-serif; font-weight: 700; color: var(--navy);
    text-transform: uppercase; line-height: 0.98;
  }
  .back-brand .line-1 { font-size: 62px; letter-spacing: 1px; }
  .back-brand .line-2 { font-size: 44px; letter-spacing: 1px; }
  .back-brand .line-3 { font-size: 16px; letter-spacing: 2px; margin-top: 6px; }
  .back-details {
    position: absolute; left: 40px; bottom: 32px;
    font-family: "Open Sans", sans-serif; font-size: 14px; color: var(--navy);
    letter-spacing: 0.3px;
  }
  .back-details .divider { margin: 0 8px; color: var(--grey); }
</style>
</head>
<body>
<main class="canvas">

  <section class="card card-front" aria-label="Business card front">
    <div class="brand">
      <span class="brand-square"></span>
      <p class="brand-name">Harbourline<br>Strategy Group</p>
    </div>

    <div class="person">
      <h1 class="person-name">Daniel Ferreira</h1>
      <p class="person-title">Principal Consultant</p>
    </div>

    <ul class="contacts">
      <li class="contact">
        <svg viewBox="0 0 24 24" aria-hidden="true"><rect x="5" y="2" width="14" height="20" rx="2.5" fill="none" stroke="var(--red)" stroke-width="2"/><line x1="10" y1="18.5" x2="14" y2="18.5" stroke="var(--red)" stroke-width="2"/></svg>
        <span>+61 417 260</span>
      </li>
      <li class="contact">
        <svg viewBox="0 0 24 24" aria-hidden="true"><rect x="2" y="4" width="20" height="16" rx="2" fill="var(--red)"/><path d="M3 6l9 7 9-7" fill="none" stroke="#fff" stroke-width="1.8"/></svg>
        <span>daniel@HarbourlineStrategyGroup.com.au</span>
      </li>
      <li class="contact">
        <svg viewBox="0 0 24 24" aria-hidden="true"><circle cx="12" cy="12" r="10" fill="var(--red)"/><ellipse cx="12" cy="12" rx="4" ry="10" fill="none" stroke="#fff" stroke-width="1.4"/><line x1="2" y1="12" x2="22" y2="12" stroke="#fff" stroke-width="1.4"/></svg>
        <span>HarbourlineStrategyGroup.com</span>
      </li>
    </ul>
  </section>

  <section class="card card-back" aria-label="Business card back">
    <div class="back-brand">
      <p class="line-1">Harbourline</p>
      <p class="line-2">Strategy Group</p>
      <p class="line-3">Pty Ltd</p>
    </div>
    <p class="back-details">A.B.N. 58210947362<span class="divider">|</span>Business Analysis, Strategic Advisory</p>
  </section>

</main>
</body>
</html>
```